New Business Card Design Project

double sided business cards. i would like to design a business card with the logo attached . that logo being centered on 1 side and then my info on the other.

Wesley Brandt CEO
Phone# 334-617-2054
Wesley@fairoakhomecare.example

Contact Information for Business Card

double sided one side the Logo attached below that saying Home Maintenance and Repair Specialists then on back my info Wesley Brandt CEO Home Maintenance Specialist Phone# 334-617-2054 Wesley@fairoakhomecare.example

Font styles to use
Serif

Colors
0054AA
0677BA
7BADD7
CADEEF
E8F1F8
FFC000
F8CF3A
FAE287
FDF2CF
FEFAEE

Requirements
Must have
• double sided logo attached on one side with colors blue and gold. black background info on the other side

```html
<!DOCTYPE html>
<html lang="en">
<head>
<meta charset="utf-8">
<title>Fair Oak Home Care – Business Card</title>
<link rel="stylesheet" href="https://fonts.googleapis.com/css2?family=Jost:wght@400;500;600&family=Roboto+Condensed:wght@700&family=Roboto:wght@400&display=swap">
<style>
  :root {
    --backdrop: #e6e7e9;
    --card-black: #000000;
    --card-white: #ffffff;
    --brand-blue: #0a72ba;
    --brand-gold: #ffc000;
    --text-grey: #5a5a5a;
    --on-dark: #ffffff;
  }
  * { margin: 0; padding: 0; box-sizing: border-box; }
  html, body {
    width: 1200px;
    height: 1000px;
    overflow: hidden;
    background: var(--backdrop);
  }
  .canvas {
    position: relative;
    width: 1200px;
    height: 1000px;
  }
  .card {
    position: absolute;
    top: 352px;
    width: 466px;
    height: 301px;
  }
  .card--front {
    left: 97px;
    background: var(--card-black);
    display: flex;
    align-items: center;
    justify-content: center;
  }
  .front-wordmark {
    font-family: "Jost", sans-serif;
    font-weight: 500;
    font-size: 40px;
    line-height: 1.1;
    letter-spacing: 2px;
    color: var(--on-dark);
    text-align: center;
    text-transform: uppercase;
  }
  .card--back {
    left: 657px;
    background: var(--card-white);
    text-align: center;
  }
  .back-brand {
    position: absolute;
    top: 56px;
    left: 0;
    width: 100%;
    display: flex;
    align-items: center;
    justify-content: center;
    gap: 10px;
  }
  .back-brand__square {
    width: 14px;
    height: 14px;
    background: var(--brand-gold);
  }
  .back-wordmark {
    font-family: "Jost", sans-serif;
    font-weight: 500;
    font-size: 24px;
    letter-spacing: 0.5px;
    color: var(--brand-blue);
    text-transform: uppercase;
  }
  .contact-name {
    position: absolute;
    top: 138px;
    left: 0;
    width: 100%;
    font-family: "Jost", sans-serif;
    font-size: 30px;
    line-height: 40px;
    color: var(--brand-blue);
  }
  .contact-name__person { font-weight: 600; }
  .contact-name__divider { font-weight: 400; margin: 0 8px; }
  .contact-name__role { font-weight: 400; }
  .contact-email {
    position: absolute;
    top: 180px;
    left: 0;
    width: 100%;
    font-family: "Roboto", sans-serif;
    font-size: 17px;
    line-height: 22px;
    letter-spacing: 1px;
    color: var(--text-grey);
  }
  .contact-phone {
    position: absolute;
    top: 233px;
    left: 0;
    width: 100%;
    display: flex;
    align-items: center;
    justify-content: center;
    gap: 7px;
    font-family: "Roboto Condensed", sans-serif;
    font-weight: 700;
    font-size: 24px;
    line-height: 30px;
    letter-spacing: 0.5px;
    color: var(--brand-blue);
  }
  .contact-phone__icon { width: 30px; height: 30px; }
</style>
</head>
<body>
<main class="canvas">
  <section class="card card--front" aria-label="Card front">
    <p class="front-wordmark">Fair Oak<br>Home Care</p>
  </section>

  <section class="card card--back" aria-label="Card back">
    <div class="back-brand">
      <span class="back-brand__square" aria-hidden="true"></span>
      <p class="back-wordmark">Fair Oak Home Care</p>
    </div>
    <p class="contact-name">
      <span class="contact-name__person">Wesley Brandt</span><span class="contact-name__divider">|</span><span class="contact-name__role">CEO</span>
    </p>
    <p class="contact-email">wesley@fairoakhomecare.example</p>
    <p class="contact-phone">
      <svg class="contact-phone__icon" viewBox="0 0 30 30" aria-hidden="true">
        <circle cx="15" cy="15" r="15" fill="var(--brand-blue)"/>
        <path d="M10.2 7.5c.5-.3 1.1-.2 1.4.3l1.7 2.8c.3.5.2 1.1-.2 1.4l-1.2 1c.8 1.8 2.2 3.3 4 4.2l1-1.2c.4-.4 1-.5 1.4-.2l2.8 1.7c.5.3.6.9.3 1.4l-1.1 1.7c-.4.6-1.1.9-1.8.8-5.3-.9-9.4-5-10.3-10.3-.1-.7.2-1.4.8-1.8z" fill="#ffffff"/>
      </svg>
      <span>334-617-2054</span>
    </p>
  </section>
</main>
</body>
</html>
```